Explainer Video Landing Page

We will soon have an "explainer" video which will explain to people in a graphical way what it is we do and the solutions we provide. Our current landing page design, located at http://www.relaynetvista.com has a lot of different elements that we like, but won't focus on the new video we have as the "hero". We will want this new landing page to really showcase the video. Some of the other design elements we need are :
1- A link to "Get a Quote Online", in some way. This is the "goal" of the landing page.
2- We'll want some content sections under the video
3- We'll want the lead gen form to be there as well.
As an example, have a look at what BrightOwl did. http://www.brightowl.com/
We like their example, but find it a bit busy. Our design should be cleaner with more whitespace. They are doing a lot of good things on that page that we'll want to mimic, like adding testimonials and existing customer logos.
Thank you in advance for participating in our design project.
Target Market(s)
Small and Mid-size Businesses. This will be a B2B landing page, focused on the communications needs of business.
Look and feel

```html
<!DOCTYPE html>
<html lang="en">
<head>
<meta charset="utf-8">
<title>Relaynet — Business phone service</title>
<link href="https://fonts.googleapis.com/css2?family=Roboto:wght@300;400;500;700;900&family=Roboto+Condensed:wght@700&display=swap" rel="stylesheet">
<style>
:root{
  --pink:#e8106a;
  --pink-dark:#c90d5b;
  --ink:#1d1d1d;
  --grey:#6b6b6b;
  --page:#f3f2f4;
  --card:#ffffff;
  --line:#d9d6da;
  --teal:#1fa8c9;
  --footer:#1e1e1e;
  --footer-text:#5e5e5e;
  --footer-head:#bdbdbd;
}
*{box-sizing:border-box;margin:0;padding:0}
html,body{width:860px;height:1200px;overflow:hidden}
body{background:var(--page);font-family:"Roboto",Arial,sans-serif;color:var(--ink);position:relative}

/* header */
.site-header{position:absolute;top:0;left:0;width:860px;height:64px;background:#f6f5f7;border-bottom:2px solid #e2e0e3}
.brand{position:absolute;left:156px;top:18px;display:flex;align-items:center;gap:8px}
.brand-mark{width:22px;height:22px;border-radius:50%;background:var(--ink)}
.brand-name{font-size:11px;font-weight:700;letter-spacing:3px;line-height:1}
.brand-tag{font-size:5px;font-weight:700;letter-spacing:.2px;margin-top:3px}
.main-nav{position:absolute;left:342px;top:26px;display:flex;gap:0;font-size:5.5px;font-weight:700;letter-spacing:.2px}
.main-nav a{color:#333;text-decoration:none;padding:3px 7px}
.main-nav a.active{background:#8c8c8c;color:#fff;border-radius:1px}
.call-box{position:absolute;left:618px;top:14px;width:62px;height:34px;border:1px solid #ddd;background:#fff;text-align:center}
.call-box .num{font-size:6px;color:#666;margin-top:3px}
.call-box .btn{margin:3px auto 0;width:56px;height:14px;background:#3a3a3a;color:#fff;font-size:6px;line-height:14px;border-radius:1px}

/* hero */
.hero{position:absolute;top:66px;left:0;width:860px;height:301px;background:linear-gradient(100deg,#3d5477 0%,#6f82a3 30%,#c9cfdb 50%,#e8ecf2 65%,#8d9cb5 85%,#5a6e8f 100%)}
.hero-video{position:absolute;left:242px;top:72px}
.video-label{position:absolute;left:180px;top:25px;width:197px;height:79px;background:var(--pink);color:#fff;padding:11px 16px 0 38px}
.video-label h2{font-family:"Roboto Condensed",Arial,sans-serif;font-size:14.5px;font-weight:700;margin-bottom:5px}
.video-label p{font-size:7px;line-height:9.5px}

/* find band */
.find-band{position:absolute;top:367px;left:0;width:860px;height:65px;background:linear-gradient(90deg,var(--pink) 0%,#f03a83 50%,var(--pink) 100%)}
.find-band h1{position:absolute;left:176px;top:6px;font-family:"Roboto Condensed",Arial,sans-serif;font-size:31px;color:#fff;letter-spacing:-.3px}
.find-band h1 span{color:var(--ink)}
.find-band .sub{position:absolute;left:178px;top:41px;font-family:"Roboto Condensed",Arial,sans-serif;font-size:12.5px;color:#fff;display:flex;gap:8px;align-items:center}
.find-band .sub b{color:var(--ink)}
.quote-btn{position:absolute;left:549px;top:18px;width:133px;height:28px;background:#1c1c1c;color:#fff;font-weight:700;font-size:9.5px;text-align:center;line-height:28px;border-radius:2px;box-shadow:0 1px 2px rgba(0,0,0,.4)}

/* plans */
.plans{position:absolute;top:468px;left:178px;display:flex;gap:10px}
.plan-card{width:118px;height:101px;background:var(--card);border:1px solid #e3e1e4;border-radius:3px;text-align:center;padding-top:12px}
.plan-card h3{font-size:6.5px;font-weight:900;letter-spacing:.5px;line-height:9px;margin-top:6px}
.plan-card p{font-size:5.8px;color:#8a8a8a;line-height:8px;margin-top:7px;padding:0 12px}
.plan-card.intro{text-align:left;padding:36px 0 0 32px}
.plan-card.intro h3{margin:0}
.tie{display:block;margin:0 auto}

.divider{position:absolute;top:587px;left:176px;width:508px;height:1px;background:var(--line)}
.divider-mark{position:absolute;top:606px;left:424px;width:12px;height:6px;border-radius:50%;background:#3a3a3a}

.intro-copy{position:absolute;top:643px;left:177px;width:508px}
.intro-copy h2{font-size:11px;font-weight:700;margin-bottom:8px}
.intro-copy p{font-size:8px;line-height:11.5px}

/* demo */
.demo-copy{position:absolute;top:750px;left:177px;width:210px}
.demo-copy h2{font-size:13.5px;font-weight:700}
.demo-copy .lead{font-size:13px;font-weight:300;margin-bottom:15px}
.demo-copy p{font-size:10px;font-weight:300;line-height:13px}
.demo-form{position:absolute;top:745px;left:435px;width:248px}
.field{height:27px;border:1px solid #cfcbd0;background:#fff;font-size:7.5px;padding:0 10px;line-height:25px;margin-bottom:11px}
.submit{width:162px;height:27px;background:var(--pink);color:#fff;font-size:13.5px;font-weight:300;text-align:center;line-height:27px;margin-top:1px}

/* footer */
.site-footer{position:absolute;top:1006px;left:0;width:860px;height:194px;background:var(--footer)}
.foot-cols{position:absolute;left:177px;top:24px;display:flex;gap:0}
.foot-col{width:131px;padding-right:15px}
.foot-col h4{font-size:7px;font-weight:400;color:var(--footer-head);padding-bottom:4px;border-bottom:1px solid #3a3a3a;margin-bottom:4px}
.foot-col a{display:block;font-size:6px;color:var(--footer-text);text-decoration:none;line-height:13px}
.social a{display:flex;align-items:center;gap:5px;line-height:16px}
.social i{width:11px;height:11px;border-radius:50%;background:#5a5a5a;display:inline-block}
.legal{position:absolute;top:156px;width:860px;text-align:center;font-size:6px;color:var(--footer-text);line-height:12px}
</style>
</head>
<body>

<header class="site-header">
  <div class="brand">
    <span class="brand-mark"></span>
    <div>
      <div class="brand-name">RELAYNET</div>
      <div class="brand-tag">Business phone service. Evolved.</div>
    </div>
  </div>
  <nav class="main-nav">
    <a class="active">HOME</a><a>PLANS &amp; PRICING</a><a>FEATURES</a><a>PHONES</a><a>LEARN MORE</a><a>BLOG</a>
  </nav>
  <div class="call-box"><div class="num">(555) 555-555</div><div class="btn">CALL ME</div></div>
</header>

<section class="hero" role="img" aria-label="Blurred city street photograph in cool blue tones">
  <div class="hero-video">
    <div class="video-label">
      <h2>THE RELAYNET VIBE</h2>
      <p>Check out Relaynet's Corporate Culture video to get a sense of the kind of people you'll be working with at Relaynet.</p>
    </div>
    <svg width="184" height="128" viewBox="0 0 184 128" style="position:absolute;left:0;top:0">
      <rect x="0" y="0" width="184" height="128" rx="34" fill="var(--pink)"/>
      <path d="M74 34 L126 64 L74 94 Z" fill="#9aa0b0"/>
    </svg>
  </div>
</section>

<section class="find-band">
  <h1>FIND US IN <span>YOUR</span> AREA.</h1>
  <div class="sub">
    <svg width="14" height="14" viewBox="0 0 14 14"><path d="M7 1 L8.5 4.5 L11 3.5 L10 7 L13 7.5 L9.5 10 L10 11 L7.5 10.5 L7.5 13.5 L6.5 13.5 L6.5 10.5 L4 11 L4.5 10 L1 7.5 L4 7 L3 3.5 L5.5 4.5 Z" fill="#fff"/></svg>
    <span>SERVICING OVER <b>950</b> CANADIAN CITIES</span>
  </div>
  <div class="quote-btn">GET A QUOTE ONLINE!</div>
</section>

<section class="plans">
  <div class="plan-card intro"><h3>SIMPLE PLANS<br>TO FIT YOUR<br>BUSINESS.</h3></div>
  <div class="plan-card">
    <svg class="tie" width="10" height="22" viewBox="0 0 10 22"><path d="M3 0h4l-1 4 3 14-4 4-4-4 3-14z" fill="var(--teal)"/></svg>
    <h3>THE<br>STANDARD</h3>
    <p>For the lone wolf trying to do business smarter than the other guy.</p>
  </div>
  <div class="plan-card">
    <svg class="tie" width="10" height="22" viewBox="0 0 10 22"><path d="M3 0h4l-1 4 3 14-4 4-4-4 3-14z" fill="var(--teal)"/><path d="M3 8l4-2M2.5 12l5-2M2 16l6-2" stroke="#fff" stroke-width="1"/></svg>
    <h3>THE<br>EXTREME</h3>
    <p>When great just ain't great enough.</p>
  </div>
  <div class="plan-card">
    <svg class="tie" width="20" height="22" viewBox="0 0 20 22"><path d="M1 6l8 4-8 4z M19 6l-8 4 8 4z" fill="#1b7fa6"/><rect x="8" y="8" width="4" height="4" fill="#1b7fa6"/></svg>
    <h3>THE<br>ULTIMATE</h3>
    <p>Every feature. Virtually unlimited everything.</p>
  </div>
</section>

<div class="divider"></div>
<div class="divider-mark"></div>

<section class="intro-copy">
  <h2>Relaynet is the Number One choice for Business VoIP Phone Service in Ottawa.</h2>
  <p>Give us a try - our Canadian-based service representatives are as comfortable talking about your phone system needs as we are discussing last night's hat trick !</p>
</section>

<section class="demo-copy">
  <h2>Not Sure?</h2>
  <div class="lead">Sign Up for a Personalized Demo.</div>
  <p>A member of Relaynet's marketing team will contact you to discuss your specific situation and see if Relaynet's Hosted PBX is a good fit for your organization. Alternatively, give us a call at 613-555-0148 to speak to someone immediately.</p>
</section>

<form class="demo-form">
  <div class="field">First name *</div>
  <div class="field">Last Name *</div>
  <div class="field">Company*</div>
  <div class="field">Phone*</div>
  <div class="field">Email*</div>
  <div class="submit">Request a demo</div>
</form>

<footer class="site-footer">
  <div class="foot-cols">
    <div class="foot-col">
      <h4>Features &amp; Benefits</h4>
      <a>Included Features</a><a>Optional Features</a><a>Conferencing</a><a>Can I keep my Phone Number?</a><a>Relaynet VoIP Phones</a><a>Money Back Guarantee</a>
    </div>
    <div class="foot-col">
      <h4>Resources</h4>
      <a>What is Hosted PBX</a><a>Frequently Asked Questions</a><a>Testimonials</a><a>Help Online</a><a>Dashboard</a>
    </div>
    <div class="foot-col">
      <h4>Relaynet</h4>
      <a>Contact Us</a><a>Media Resources</a><a>Our History</a><a>Jobs</a><a>Relaynet Vibe</a><a>RelayTalk, our Blog</a>
    </div>
    <div class="foot-col social">
      <h4>Social</h4>
      <a><i></i>Friendbook</a><a><i></i>Chirper</a><a><i></i>ClipStream</a><a><i></i>Circles+</a><a><i></i>ProLink</a>
    </div>
  </div>
  <div class="legal">Call 1 877 55 RELAY or email sales@relaynet.example<br>Copyright © 2014 Relaynet. All rights reserved. This site has a Privacy policy.</div>
</footer>

</body>
</html>
```